Bright Harbor Workshops business card design

Needing a business card design using an existing logo. Double sided card and we will be printing using rounded corners. Can also use metallics if appropriate. The design needs to be professional and modern.

Target Market(s)

Professional organisations

Industry/Entity Type

Business

Contact Information for Business Card

busines name, person name, email, website, phone, address,

Colors

Designer to choose colors to be used in the design.

Requirements
Must have
• Use existing 'Bright Harbor Workshops' logo Using uploaded logo design. Simple and modern design. Black,white,silver,greys as the dominant colouring. Can introduce another single colour. Must also include a small version of the attached 'KDL' logo on the card (white and black versions uploaded also)
Nice to have
• Something modern
Should not have
• Additional images

```html
<!DOCTYPE html>
<html lang="en">
<head>
<meta charset="utf-8">
<title>Bright Harbor Workshops — Business Card</title>
<link href="https://fonts.googleapis.com/css2?family=Crimson+Text:wght@400;600;700&display=swap" rel="stylesheet">
<style>
  :root {
    --backdrop: #0f161d;
    --silver-edge: #a6a9aa;
    --silver-mid: #c5cacb;
    --ink: #151515;
    --panel: #0b0b0b;
    --panel-text: #d2d2d2;
    --name-text: #c9c9c9;
  }
  * { margin: 0; padding: 0; box-sizing: border-box; }
  html, body { width: 1200px; height: 1000px; overflow: hidden; }
  body {
    background: var(--backdrop);
    font-family: "Crimson Text", Georgia, serif;
    color: var(--ink);
    position: relative;
  }
  .card {
    position: absolute;
    left: 260px;
    width: 680px;
    height: 386px;
    border-radius: 32px;
    overflow: hidden;
    background: linear-gradient(180deg, var(--silver-edge) 0%, var(--silver-mid) 55%, var(--silver-edge) 100%);
    box-shadow: 0 4px 14px rgba(0,0,0,0.5);
  }
  .card-front { top: 104px; }
  .card-back { top: 530px; }

  .wordmark {
    position: absolute;
    text-align: right;
    font-weight: 400;
    text-transform: uppercase;
    letter-spacing: 2px;
    line-height: 1;
    color: var(--ink);
  }
  .tagline {
    position: absolute;
    font-weight: 700;
    white-space: nowrap;
    color: var(--ink);
  }
  .card-front .wordmark { right: 198px; top: 138px; font-size: 44px; }
  .card-front .wordmark span { display: block; height: 48px; }
  .card-front .tagline { left: 186px; top: 282px; font-size: 16px; }

  .card-back .wordmark { right: 422px; top: 66px; font-size: 36px; }
  .card-back .wordmark span { display: block; height: 38px; }
  .card-back .tagline { left: 32px; top: 179px; font-size: 12.5px; }

  .panel {
    position: absolute;
    inset: 0;
  }
  .contact-name {
    position: absolute;
    right: 26px; top: 52px;
    font-size: 27px; font-weight: 600;
    color: var(--name-text);
    letter-spacing: 1px;
  }
  .contact-role {
    position: absolute;
    right: 26px; top: 84px;
    font-size: 19px;
    color: var(--name-text);
  }
  .contact-list {
    position: absolute;
    right: 24px; top: 266px;
    list-style: none;
    text-align: right;
  }
  .contact-list li {
    font-size: 19px;
    line-height: 24.5px;
    color: var(--panel-text);
    display: flex; justify-content: flex-end; align-items: center; gap: 8px;
  }
  .contact-list svg { width: 16px; height: 16px; fill: var(--panel-text); }

  .member-badge {
    position: absolute;
    left: 26px; top: 318px;
    display: flex; align-items: flex-end; gap: 8px;
  }
  .member-mark { display: flex; flex-direction: column; align-items: center; }
  .member-mark .dot { width: 22px; height: 22px; border-radius: 50%; background: var(--ink); margin-bottom: 2px; }
  .member-mark .label { font-size: 15px; font-weight: 400; line-height: 1; }
  .member-divider { width: 1px; height: 40px; background: var(--ink); }
  .member-text { font-size: 8.5px; line-height: 9px; }
</style>
</head>
<body>
  <section class="card card-front">
    <div class="wordmark"><span>Bright</span><span>Harbor</span><span>Workshops</span></div>
    <div class="tagline">Evidence-Based Training &amp; Development</div>
  </section>

  <section class="card card-back">
    <div class="wordmark"><span>Bright</span><span>Harbor</span><span>Workshops</span></div>
    <div class="tagline">Evidence-Based Training &amp; Development</div>

    <svg class="panel" width="680" height="386" viewBox="0 0 680 386" role="img" aria-label="Large dark decorative silhouette area">
      <path d="M360 0 H680 V386 H340 C320 330 300 280 300 240 C300 200 280 190 282 170 C284 120 320 60 360 0 Z" fill="var(--panel)"/>
    </svg>

    <div class="contact-name">ALEX MORGAN</div>
    <div class="contact-role">Director</div>
    <ul class="contact-list">
      <li>(21)-5550-4817 <svg viewBox="0 0 16 16"><path d="M4 0h8a1.5 1.5 0 0 1 1.5 1.5v13A1.5 1.5 0 0 1 12 16H4a1.5 1.5 0 0 1-1.5-1.5v-13A1.5 1.5 0 0 1 4 0zm0 2v10h8V2zm4 11a1 1 0 1 0 0 2 1 1 0 0 0 0-2z" fill-rule="evenodd"/></svg></li>
      <li>(21)-5550-4817 <svg viewBox="0 0 16 16"><path d="M1 5c0-2 3-3 7-3s7 1 7 3v1.5h-3.5V5h-7v1.5H1zM3 8h10l1.5 6.5h-13zm5 1.5a2 2 0 1 0 0 4 2 2 0 0 0 0-4z" fill-rule="evenodd"/></svg></li>
      <li>alex@brightharbor.com <svg viewBox="0 0 16 16"><path d="M0 3h16v10H0zm1.5 1.3v7.4L6 8zm13 0L10 8l4.5 3.7zM2 3.8 8 9l6-5.2z" fill-rule="evenodd"/></svg></li>
      <li>www.bhw.com <svg viewBox="0 0 16 16"><path d="M8 0a8 8 0 1 1 0 16A8 8 0 0 1 8 0zm-2 3C4 4 3.5 6 4.5 7s2.5 0 3 1.5S6 12 7.5 13s2.5-1.5 2.5-3 2-1.5 2.5-3S10 3 8.5 3.5 7 2.5 6 3z" fill-rule="evenodd"/></svg></li>
    </ul>

    <div class="member-badge">
      <div class="member-mark">
        <div class="dot"></div>
        <div class="label">KDL</div>
      </div>
      <div class="member-divider"></div>
      <div class="member-text">Member<br>Kestrel<br>Development<br>League KDL</div>
    </div>
  </section>
</body>
</html>
```